Modern and strong website design for a Dutch crowdsourcing company
.

We are startup company providing crowdsourcing of administrative and customers service tasks for larger companies and other organizations. We offer cost savings and scale-ability combined with higher quality of execution. We will soon enter the market and need a website that has two major target groups: 1. Our corporate customers 2. The mainly younger crowd executing the tasks on our platform.
The target group of customers are Influencers and decision makers with companies and other organizations in with large administrative and customer service departments. Most information in the startup phase will be targeting this group.
The target group of future crowd workers will be heterogeneous, from students to stay at home mums or night shift workers who want to earn some extra money by performing easy to execute microtasks in the cloud. We will target both Dutch and international workers.

The website must be developed for browsing on a computer but also be optimized for mobile devices and tablets.
The website must be optimized and tested for the major browsers on windows, macOS and mobile devices.

For the minimum requirement for the website see attached wireframes

The present landing page http://bravolinkhive.com and logo are not reflecting our preferences!
See enclosed a new logo that stands for both the crowdwork (performed for our customers) and the crowd (a hive in motion).

Target Market(s)

see tekst above.

Industry/Entity Type

Business Service

Coding

Coded - Design and coding required

Number of Pages Required

5+ page

Font styles to use
Sans Serif
Other font styles liked:
• Lato, Open Sans

Colors

Designer to choose colors to be used in the design.

Requirements
Must have
• start devider screen
• home page displaying business and worker information
• a page displaying only info for businesses
• a page displaying only info for workers
• a contact form
• a reviews page
• color scheme from logo
• responsiveness!
Nice to have
• Nice animations
• overlapping blocks, animated on scroll
• lightbox effects if applicable
• animated mobile menu icon and menu itself

```html
<!DOCTYPE html>
<html lang="en">
<head>
<meta charset="utf-8">
<title>A Hive in Motion – Start</title>
<link rel="stylesheet" href="https://fonts.googleapis.com/css2?family=Poppins:wght@500;600;700&family=Open+Sans:wght@400;600&display=swap">
<style>
  :root {
    --hero-dark: #1f1b19;
    --hero-mid: #3a3431;
    --hero-warm: #4a3428;
    --white: #ffffff;
    --orange: #f26c0f;
    --grey-button: #7a7a7a;
    --footer-bg: #7b7b7b;
  }
  * { box-sizing: border-box; margin: 0; padding: 0; }
  html, body { width: 1200px; height: 763px; overflow: hidden; }
  body { position: relative; font-family: "Open Sans", Arial, sans-serif; color: var(--white); background: var(--footer-bg); }

  .hero { position: absolute; left: 0; top: 0; width: 1200px; height: 636px; overflow: hidden; }
  .hero-photo {
    position: absolute; inset: 0;
    background:
      radial-gradient(ellipse at 50% 40%, rgba(90,80,72,0.55), transparent 65%),
      linear-gradient(90deg, var(--hero-mid) 0%, var(--hero-dark) 45%, var(--hero-warm) 80%, var(--hero-dark) 100%);
  }
  .brand-name {
    position: absolute; left: 0; width: 1200px; top: 200px; text-align: center;
    font-family: "Poppins", Arial, sans-serif; font-weight: 700; font-size: 56px; line-height: 1;
    letter-spacing: -0.5px;
  }
  .for-label {
    position: absolute; left: 0; width: 1200px; top: 346px; text-align: center;
    font-family: "Poppins", Arial, sans-serif; font-weight: 600; font-size: 24px; letter-spacing: 1px;
  }
  .audience-button {
    position: absolute; top: 421px; width: 161px; height: 41px;
    display: flex; align-items: center; justify-content: center;
    font-family: "Poppins", Arial, sans-serif; font-weight: 600; font-size: 18px; letter-spacing: 0.5px;
    color: var(--white); text-decoration: none; border-radius: 2px;
  }
  .audience-button.workers { left: 429px; background: var(--orange); }
  .audience-button.business { left: 609px; background: var(--grey-button); }

  .site-footer { position: absolute; left: 0; top: 636px; width: 1200px; height: 127px; background: var(--footer-bg); }
  .footer-mark { position: absolute; left: 97px; top: 45px; width: 40px; height: 40px; border-radius: 50%; background: var(--white); }
  .contact-line { position: absolute; left: 150px; display: flex; align-items: center; gap: 9px; white-space: nowrap; }
  .contact-line.phone { top: 44px; font-size: 14px; font-weight: 600; }
  .contact-line.email { top: 72px; font-size: 13px; }
  .contact-line svg { width: 14px; height: 14px; fill: var(--white); }
  .footer-nav { position: absolute; left: 480px; top: 56px; display: flex; gap: 18px; font-size: 14px; font-weight: 600; }
  .footer-nav a { color: var(--white); text-decoration: none; }
  .copyright { position: absolute; left: 804px; top: 40px; font-size: 12.5px; white-space: nowrap; }
  .social-links { position: absolute; left: 1003px; top: 70px; display: flex; gap: 7px; }
  .social-links span { width: 28px; height: 28px; border-radius: 50%; background: var(--white); display: block; }
</style>
</head>
<body>
  <section class="hero">
    <div class="hero-photo" role="img" aria-label="Dimmed photo of an open-plan office with people working at computers"></div>
    <h1 class="brand-name">A Hive in Motion</h1>
    <p class="for-label">FOR</p>
    <a class="audience-button workers" href="#">WORKERS</a>
    <a class="audience-button business" href="#">BUSINESS</a>
  </section>

  <footer class="site-footer">
    <span class="footer-mark" aria-hidden="true"></span>
    <div class="contact-line phone">
      <svg viewBox="0 0 24 24" aria-hidden="true"><path d="M6.6 10.8a15.1 15.1 0 0 0 6.6 6.6l2.2-2.2a1 1 0 0 1 1-.25 11.4 11.4 0 0 0 3.6.57 1 1 0 0 1 1 1V20a1 1 0 0 1-1 1A17 17 0 0 1 3 4a1 1 0 0 1 1-1h3.5a1 1 0 0 1 1 1c0 1.25.2 2.45.57 3.6a1 1 0 0 1-.25 1z"/></svg>
      <span>Phone: 0698765432</span>
    </div>
    <div class="contact-line email">
      <svg viewBox="0 0 24 24" aria-hidden="true"><path d="M2 6h20v1l-10 6L2 7z"/><path d="M2 9l10 6 10-6v9H2z"/></svg>
      <span>info@bravolinkhive.com</span>
    </div>
    <nav class="footer-nav">
      <a href="#">Home</a>
      <a href="#">For Workers</a>
      <a href="#">For Business</a>
    </nav>
    <p class="copyright">Copyright © A Hive in Motion. All rights reserved.</p>
    <div class="social-links" aria-label="Social media">
      <span></span><span></span><span></span>
    </div>
  </footer>
</body>
</html>
```